Luxury Business Card Design for High-End Window Treatments

Gilded Vantages
Custom Plantation Shutters & Architectural Shading Systems

⸻

BACK

Daniel Forsythe
Owner

Custom Interior & Exterior Window Treatments

919-482-7034
gildedvantages.com

I have included a picture that I’m hoping we can use on the back, but I’m also wondering if you can get rid of the ladder? Should we get rid of shutters , shades and blinds underneath Gilded Vantages?

Target Market(s)

High-end residential homeowners, custom home builders, architects, interior designers, and luxury renovation clients seeking premium plantation shutters and motorized architectural shading systems.

Industry/Entity Type

Custom Window treatments

Contact Information for Business Card

Front Gilded Vantages Custom Plantation Shutters Motorized Architectural Shading Systems BACK Daniel Forsythe Owner 919-482-7034 GildedVantages.com Custom Interior & Exterior Window Treatments By Appointment

Requirements
Nice to have
• Not 100% sure on nice to halves or the color but you can definitely check out my website to get a better understanding of what I’m trying to do

```html
<!DOCTYPE html>
<html lang="en">
<head>
<meta charset="UTF-8">
<title>Gilded Vantages — Business Cards</title>
<link rel="stylesheet" href="https://fonts.googleapis.com/css2?family=Cormorant+Garamond:wght@600;700&family=Montserrat:wght@400;500;700&display=swap">
<style>
  :root {
    --backdrop: #bdbdbd;
    --card-black: #050505;
    --gold: #cdb45a;
    --gold-edge: #d8c062;
    --white: #f4f4f4;
    --sky: #6f9fd6;
    --foliage: #3d4a2a;
    --stone: #6b5a48;
  }
  * { box-sizing: border-box; margin: 0; padding: 0; }
  html, body { width: 1200px; height: 815px; overflow: hidden; }
  body {
    background: linear-gradient(160deg, #d6d6d6, var(--backdrop) 60%, #a9a9a9);
    font-family: "Montserrat", sans-serif;
    position: relative;
  }
  .card {
    position: absolute;
    top: 250px;
    width: 540px;
    height: 310px;
    border-radius: 22px;
    background: var(--card-black);
    border: 3px solid var(--gold-edge);
    overflow: hidden;
    box-shadow: 0 14px 30px rgba(0,0,0,0.35);
  }
  .card--back { left: 40px; }
  .card--front { left: 620px; }

  /* back side */
  .card__photo {
    position: absolute;
    top: 0; right: 0;
    width: 66%;
    height: 100%;
    background: linear-gradient(180deg, var(--sky) 0%, #8fb6e0 25%, var(--stone) 50%, var(--foliage) 80%, #1f2414 100%);
  }
  .card__photo-fade {
    position: absolute;
    inset: 0;
    background:
      linear-gradient(90deg, var(--card-black) 0%, rgba(5,5,5,0.85) 18%, rgba(5,5,5,0) 55%),
      linear-gradient(0deg, var(--card-black) 0%, rgba(5,5,5,0.7) 25%, rgba(5,5,5,0) 55%);
  }
  .back-content {
    position: absolute;
    left: 28px;
    bottom: 24px;
  }
  .brand-name {
    font-family: "Cormorant Garamond", serif;
    font-weight: 700;
    color: var(--gold);
    line-height: 1;
  }
  .back-content .brand-name { font-size: 30px; }
  .brand-tagline {
    font-family: "Cormorant Garamond", serif;
    font-weight: 700;
    color: var(--gold);
    letter-spacing: 0.5px;
  }
  .back-content .brand-tagline { font-size: 14px; margin-top: 4px; word-spacing: 10px; }
  .person-name {
    margin-top: 18px;
    font-weight: 700;
    font-size: 22px;
    color: var(--gold);
  }
  .person-role {
    font-size: 12px;
    color: var(--white);
    margin-top: 1px;
  }
  .contact-list {
    list-style: none;
    margin-top: 14px;
  }
  .contact-list li {
    display: flex;
    align-items: center;
    gap: 8px;
    font-size: 12px;
    color: var(--white);
    line-height: 19px;
  }
  .contact-list svg { width: 11px; height: 11px; flex: none; }
  .contact-list .domain { color: var(--gold); }

  /* front side */
  .front-content {
    position: absolute;
    inset: 0;
    display: flex;
    flex-direction: column;
    align-items: center;
    justify-content: center;
    text-align: center;
  }
  .front-content .brand-name { font-size: 54px; }
  .front-content .brand-tagline { font-size: 22px; margin-top: 10px; word-spacing: 18px; }
  .service-line {
    margin-top: 36px;
    font-size: 14px;
    color: var(--white);
  }
</style>
</head>
<body>

  <section class="card card--back" aria-label="Card back">
    <div class="card__photo" role="img" aria-label="Photograph of a two-storey home with a screened porch and white trim, trees and blue sky"></div>
    <div class="card__photo-fade"></div>
    <div class="back-content">
      <p class="brand-name">Gilded Vantages</p>
      <p class="brand-tagline">Shutters Shades Blinds</p>
      <p class="person-name">Daniel Forsythe</p>
      <p class="person-role">Owner</p>
      <ul class="contact-list">
        <li>
          <svg viewBox="0 0 12 12" aria-hidden="true"><rect x="3" y="0.5" width="6" height="11" rx="1.2" fill="none" stroke="var(--gold)" stroke-width="1.2"/></svg>
          919-482-7034
        </li>
        <li>
          <svg viewBox="0 0 12 12" aria-hidden="true"><rect x="0.5" y="2" width="11" height="8" fill="var(--gold)"/><path d="M0.5 2 L6 7 L11.5 2" fill="none" stroke="var(--card-black)" stroke-width="1"/></svg>
          info@gildedvantages.com
        </li>
        <li>
          <svg viewBox="0 0 12 12" aria-hidden="true"><circle cx="6" cy="6" r="5.3" fill="none" stroke="var(--gold)" stroke-width="1.2"/><path d="M0.7 6 H11.3 M6 0.7 V11.3 M6 0.7 C3 4 3 8 6 11.3 M6 0.7 C9 4 9 8 6 11.3" fill="none" stroke="var(--gold)" stroke-width="0.9"/></svg>
          <span>www.<span class="domain">gildedvantages</span>.com</span>
        </li>
      </ul>
    </div>
  </section>

  <section class="card card--front" aria-label="Card front">
    <div class="front-content">
      <p class="brand-name">Gilded Vantages</p>
      <p class="brand-tagline">Shutters Shades Blinds</p>
      <p class="service-line">Custom Interior &amp; Exterior Window Treatments</p>
    </div>
  </section>

</body>
</html>
```